Business card design needed

Our modern electrical contracting company requires business card design utilising our logo and incorporating our tag line "Service when you need it". We specialise in assisting our customers 24/7 offering a breakdown service.

Industry/Entity Type

Electrical

Contact Information for Business Card

Marcus Penhale, Electrical contractor,Tel: (08) 8456 3071, Fax: (08) 8679 4315, Mob 0438 562 740, Email: marcus.penhale@brightwirepower.com.au, Web: www.brightwirepower.com.au

Requirements
Must have
• we require a 2 sided card.
Front- Logo, tag line and contact information.
Rear- service when you need it! Call now for our 24/7 breakdown service

```html
<!DOCTYPE html>
<html lang="en">
<head>
<meta charset="utf-8">
<title>Brightwire Power – Business Card Rear</title>
<link rel="stylesheet" href="https://fonts.googleapis.com/css2?family=Roboto:ital,wght@0,900;1,900&display=swap">
<style>
  :root {
    --paper: #ffffff;
    --carbon-dark: #1c1f20;
    --carbon-mid: #383d3f;
    --brand-blue: #1f4fd8;
    --ink-dark: #262829;
    --ink-edge: #a9aeb1;
    --monogram: #eef0f0;
    --accent-circle: #2a5ee0;
  }
  * { margin: 0; padding: 0; box-sizing: border-box; }
  html, body {
    width: 1200px;
    height: 741px;
    overflow: hidden;
    background: var(--paper);
  }
  .card {
    position: relative;
    width: 1200px;
    height: 741px;
    background: var(--paper);
    overflow: hidden;
    font-family: "Roboto", Arial, sans-serif;
  }
  .backdrop {
    position: absolute;
    inset: 0;
    width: 1200px;
    height: 741px;
  }
  .backdrop__monogram {
    font-family: "Roboto", Arial, sans-serif;
    font-weight: 900;
    fill: var(--monogram);
  }
  .brand-mark {
    position: absolute;
    left: 442px;
    top: 97px;
    width: 233px;
    height: 233px;
    border-radius: 50%;
    background: var(--accent-circle);
  }
  .company-name {
    position: absolute;
    left: 125px;
    top: 372px;
    white-space: nowrap;
    font-weight: 900;
    font-size: 89px;
    line-height: 1;
    color: var(--brand-blue);
    letter-spacing: 0.5px;
  }
  .tagline {
    position: absolute;
    white-space: nowrap;
    font-style: italic;
    font-weight: 900;
    color: var(--ink-dark);
    line-height: 1;
    text-shadow:
      -1px -1px 0 var(--ink-edge),
      1px -1px 0 var(--ink-edge),
      -1px 1px 0 var(--ink-edge),
      3px 4px 4px rgba(0,0,0,0.45);
  }
  .tagline--primary {
    left: 275px;
    top: 503px;
    font-size: 54px;
    letter-spacing: -0.5px;
  }
  .tagline--call {
    left: 208px;
    top: 578px;
    font-size: 50px;
    letter-spacing: -0.5px;
  }
  .tagline__highlight {
    color: var(--brand-blue);
  }
</style>
</head>
<body>
  <main class="card">
    <svg class="backdrop" viewBox="0 0 1200 741" role="img" aria-label="Faint large company initials behind a dark carbon-fibre textured diagonal panel">
      <defs>
        <linearGradient id="carbonShade" x1="0" y1="0" x2="1" y2="1">
          <stop offset="0" stop-color="#383d3f"/>
          <stop offset="1" stop-color="#1c1f20"/>
        </linearGradient>
      </defs>
      <text class="backdrop__monogram" x="150" y="690" font-size="920" textLength="960" lengthAdjust="spacingAndGlyphs">BP</text>
      <polygon points="18,18 762,18 135,668 18,668" fill="url(#carbonShade)"/>
    </svg>

    <div class="brand-mark" aria-hidden="true"></div>
    <h1 class="company-name">BRIGHTWIRE POWER</h1>

    <p class="tagline tagline--primary">service when you need it!</p>
    <p class="tagline tagline--call">Call now for our <span class="tagline__highlight">24/7</span> breakdown service</p>
  </main>
</body>
</html>
```